Web Design for ORV Air conditioning company

Hello,

I am calling on you for the modernization of the company's website
https://clim-solaris-atelier.fr/

The new one must include the new logo with the new graphic charter (color, style ...)

I'm looking for a simple design (less is more), a font written without Serif, the logo that brings a touch of color and modernity.

(maintenance and installation company for air conditioning and ventilation systems)
COLORS: in line with the logo

CHAPTER:

# PRESENTATION
# SERVICES
AIR CONDITIONING (ice cube icon)
HEATING (flame icon)
AIR TREATMENT (icon fan)
# ACHIEVEMENTS

# CONTACT
CONTACT FORM
GOOGLE MAPS

Target Market(s)

Showcase site for our customers

Coding

Coded - Design and coding required

Number of Pages Required

4 page

Font styles to use
Sans Serif

Colors
33b8a4
33a6d7
3176b5
ffffff

Requirements
Must have
• Clear and fluid navigation
a visual identity of the page with the logo
Should not have
• Overloaded.

```html
<!DOCTYPE html>
<html lang="en">
<head>
<meta charset="utf-8">
<title>ORV – Air conditioning</title>
<link href="https://fonts.googleapis.com/css2?family=Montserrat:wght@500;600;700;800;900&family=Lato:wght@400;700&display=swap" rel="stylesheet">
<style>
:root{
  --green:#3cc186;
  --teal:#33b8a4;
  --blue:#2a8fc1;
  --sky:#33a6d7;
  --navy:#3176b5;
  --ink:#222;
  --slate:#2d3e48;
  --grey:#6b7780;
  --light:#f3f3f3;
  --white:#ffffff;
}
*{margin:0;padding:0;box-sizing:border-box}
html,body{width:1200px;height:2822px;overflow:hidden;background:var(--white)}
body{position:relative;font-family:'Lato',sans-serif;color:var(--ink)}
.abs{position:absolute}
.brand{font-family:'Montserrat',sans-serif;font-weight:900;color:var(--slate);display:flex;align-items:center;gap:10px;letter-spacing:2px}
.brand .dot{width:18px;height:18px;background:var(--teal)}
.header .brand{left:110px;top:20px;font-size:52px}
.tagline{left:243px;top:58px;font-family:'Montserrat',sans-serif;font-weight:600;font-size:16px;color:#6d8a96}
.topline{right:112px;top:16px;font-family:'Montserrat',sans-serif;font-weight:500;font-size:17px;display:flex;gap:14px;align-items:center}
.topline svg{vertical-align:-2px;margin-right:6px}
.nav{right:112px;top:58px;display:flex;gap:23px;font-family:'Montserrat',sans-serif;font-weight:700;font-size:17px}
.nav a{color:var(--ink);text-decoration:none;position:relative}
.nav a.active::after{content:"";position:absolute;left:0;right:0;bottom:-10px;height:4px;background:var(--green)}
.hero{left:0;top:105px;width:1200px;height:650px}
.hero-title{left:110px;top:165px;font-family:'Montserrat',sans-serif;font-weight:900;font-size:62px;line-height:74px;color:var(--ink)}
.btn{display:flex;align-items:center;justify-content:center;background:var(--green);color:var(--white);font-family:'Montserrat',sans-serif;font-weight:700}
.quote{left:113px;top:412px;width:220px;height:60px;font-size:20px}
.dots{left:564px;top:642px;display:flex;gap:8px}
.dots span{width:12px;height:12px;background:#9aa3a8}
.dots span:first-child{background:var(--ink)}
.section-title{left:0;width:1200px;text-align:center;font-family:'Montserrat',sans-serif;font-weight:900;font-size:56px}
.card{width:311px;height:353px;top:895px;text-align:center}
.card svg.frame{position:absolute;left:0;top:0}
.card .icon{position:absolute;left:0;right:0;top:70px;display:flex;justify-content:center}
.card h3{position:absolute;left:0;right:0;top:178px;font-family:'Montserrat',sans-serif;font-weight:600;font-size:22px}
.card p{position:absolute;left:22px;right:22px;top:216px;font-size:16.5px;line-height:26px;color:var(--grey)}
.card .more{position:absolute;left:0;right:0;top:309px;font-family:'Montserrat',sans-serif;font-weight:700;font-size:17px;color:var(--green)}
.card.featured h3,.card.featured p,.card.featured .more{color:var(--white)}
.cert{top:1544px;width:231px;height:278px;background:var(--white);box-shadow:0 2px 6px rgba(0,0,0,.12);padding:6px}
.cert div{width:100%;height:100%}
.arrow{top:1660px}
.contact-bg{left:0;top:1907px;width:1200px;height:915px;background:linear-gradient(160deg,#4cb77f 0%,#2f9c98 45%,#2b8bc6 100%)}
.sub{font-family:'Montserrat',sans-serif;font-weight:600;font-size:27px;color:var(--white);top:2045px}
.field{background:#2a6868;color:var(--white);font-size:17px;padding:14px 20px;border-radius:2px}
.send{left:112px;top:2365px;width:128px;height:58px;font-size:23px;font-weight:800}
.map{left:744px;top:2111px;width:346px;height:309px;background:linear-gradient(135deg,#eef0ee,#dfe5e3)}
.footer-logo{left:0;width:1200px;top:2528px;display:flex;justify-content:center}
.footer-logo .brand{font-size:84px}
.footer-logo .brand .dot{width:26px;height:26px}
.info{top:2643px;display:flex;align-items:center;gap:14px;font-size:17px;color:#555;line-height:30px}
.info .ring{width:48px;height:48px;border:1px solid #ccc;border-radius:50%;display:flex;align-items:center;justify-content:center}
.links{left:0;width:1200px;top:2725px;text-align:center;font-size:17px;color:#444}
.links span{margin:0 18px}
.copy{left:0;width:1200px;top:2768px;text-align:center;font-size:17px;color:#444}
.social{left:1155px;top:2636px;width:45px;height:112px;background:#555;display:flex;flex-direction:column;align-items:center;justify-content:space-around;padding:6px 0}
.social span{width:14px;height:14px;background:var(--white);border-radius:3px}
</style>
</head>
<body>

<header class="header">
  <div class="abs brand"><span>ORV</span><span class="dot"></span></div>
  <div class="abs tagline">OPTIMA RÉSEAU VENTILATION</div>
  <div class="abs topline">
    <span><svg width="16" height="12" viewBox="0 0 16 12"><rect width="16" height="12" fill="#3cc186"/><path d="M0 0l8 6 8-6" stroke="#fff" stroke-width="1.5" fill="none"/></svg>contact.orv@atelier-mail.fr</span>
    <span>|</span>
    <span><svg width="14" height="14" viewBox="0 0 24 24"><path fill="#3cc186" d="M6.6 10.8a15 15 0 006.6 6.6l2.2-2.2c.3-.3.7-.4 1-.2 1.1.4 2.3.6 3.6.6.6 0 1 .4 1 1V20c0 .6-.4 1-1 1A17 17 0 013 4c0-.6.4-1 1-1h3.5c.6 0 1 .4 1 1 0 1.3.2 2.5.6 3.6.1.3 0 .7-.2 1z"/></svg>04 71 23 45 60</span>
  </div>
  <nav class="abs nav">
    <a class="active">HOME</a><a>ABOUT US</a><a>SERVICES</a><a>ACHIEVEMENTS</a><a>CONTACT</a>
  </nav>
</header>

<section>
  <svg class="abs hero" width="1200" height="650" viewBox="0 0 1200 650">
    <defs>
      <linearGradient id="heroPhoto" x1="0" y1="0" x2="1" y2="1">
        <stop offset="0" stop-color="#e9ebec"/><stop offset=".6" stop-color="#cfd3d6"/><stop offset="1" stop-color="#b8bdc1"/>
      </linearGradient>
      <linearGradient id="band" x1="0" y1="0" x2="1" y2="0">
        <stop offset="0" stop-color="#3cc186"/><stop offset=".5" stop-color="#33b8a4"/><stop offset="1" stop-color="#2a8fc1"/>
      </linearGradient>
    </defs>
    <rect width="1200" height="650" fill="url(#heroPhoto)" role="img" aria-label="Photo of a white radiator with a thermostatic valve"/>
    <path d="M0 475 L598 610 L1200 475 L1200 650 L0 650Z" fill="#fff"/>
    <path d="M0 475 L598 610 L1200 475 L1200 510 L598 645 L0 510Z" fill="url(#band)"/>
  </svg>
  <h1 class="abs hero-title">OPTIMA<br>NETWORK<br>VENTILATION</h1>
  <div class="abs btn quote">GET A QUOTE</div>
  <div class="abs dots"><span></span><span></span><span></span><span></span></div>
</section>

<section>
  <h2 class="abs section-title" style="top:808px">SERVICES</h2>

  <div class="abs card" style="left:112px">
    <svg class="frame" width="311" height="353"><path d="M.5 .5 L155 58 L310.5 .5 V352.5 H.5Z" fill="#fff" stroke="#999"/></svg>
    <div class="icon"><svg width="90" height="82" viewBox="0 0 90 82" fill="none" stroke="#2a8fc1" stroke-width="3" stroke-linejoin="round"><path d="M10 8l16-6 16 6-16 6z M10 8v16l16 6 16-6V8 M26 14v16"/><path d="M44 26l16-6 16 6-16 6z M44 26v18l16 6 16-6V26 M60 32v18"/><path d="M4 46l16-6 16 6-16 6z M4 46v18l16 6 16-6V46 M20 52v18"/></svg></div>
    <h3>AIR CONDITIONING</h3>
    <p>Temporibus autem quibusdut officiis debitis aut rerum necessitati bus saepe evenietuptreda</p>
    <div class="more">READ MORE</div>
  </div>

  <div class="abs card featured" style="left:445px">
    <svg class="frame" width="311" height="353"><path d="M0 0 L155 58 L311 0 V353 H0Z" fill="#2a8fc1"/></svg>
    <div class="icon"><svg width="66" height="86" viewBox="0 0 66 86" fill="none" stroke="#fff" stroke-width="3" stroke-linejoin="round"><path d="M30 3c4 16 30 24 30 50a27 27 0 01-54 0c0-12 6-20 12-25 0 8 3 13 7 15-2-14 0-28 5-40z"/><path d="M33 50c2 8 12 12 12 21a12 12 0 01-24 0c0-6 4-9 6-11 1 4 2 5 3 6 0-6 1-11 3-16z"/></svg></div>
    <h3>HEATING</h3>
    <p>Temporibus autem quibusdut officiis debitis aut rerum necessitati bus saepe evenietuptreda</p>
    <div class="more">READ MORE</div>
  </div>

  <div class="abs card" style="left:778px">
    <svg class="frame" width="311" height="353"><path d="M.5 5 L155 60 L310.5 5 V352.5 H.5Z" fill="#fff" stroke="#999"/></svg>
    <div class="icon"><svg width="82" height="82" viewBox="0 0 82 82" fill="none" stroke="#2a8fc1" stroke-width="3"><circle cx="41" cy="41" r="7"/><path d="M41 34C30 28 28 10 40 6c12-4 18 12 7 24"/><path d="M48 41c6-11 24-13 28-1 4 12-12 18-24 7"/><path d="M41 48c11 6 13 24 1 28-12 4-18-12-7-24"/><path d="M34 41c-6 11-24 13-28 1-4-12 12-18 24-7"/></svg></div>
    <h3>AIR TREATMENT</h3>
    <p>Temporibus autem quibusdut officiis debitis aut rerum necessitati bus saepe evenietuptreda</p>
    <div class="more">READ MORE</div>
  </div>
</section>

<section>
  <svg class="abs" style="left:0;top:1330px" width="1200" height="577"><path d="M0 137 L600 0 L1200 137 V577 H0Z" fill="#f3f3f3"/></svg>
  <h2 class="abs section-title" style="top:1444px">ACHIEVEMENTS</h2>
  <svg class="abs arrow" style="left:56px" width="20" height="34"><path d="M17 2L3 17l14 15" stroke="#888" stroke-width="3" fill="none"/></svg>
  <svg class="abs arrow" style="left:1122px" width="20" height="34"><path d="M3 2l14 15L3 32" stroke="#888" stroke-width="3" fill="none"/></svg>
  <div class="abs cert" style="left:112px"><div role="img" aria-label="Scan of a business advisor certificate" style="background:linear-gradient(160deg,#eee,#e2e2e2)"></div></div>
  <div class="abs cert" style="left:360px"><div role="img" aria-label="Scan of a certificate of certification" style="background:linear-gradient(90deg,#34508a 0 12%,#f4efe0 12%)"></div></div>
  <div class="abs cert" style="left:608px"><div role="img" aria-label="Scan of a quality management certificate" style="background:linear-gradient(160deg,#f5f7fa,#e7edf2)"></div></div>
  <div class="abs cert" style="left:855px"><div role="img" aria-label="Scan of an ISO 9001 registration certificate" style="background:linear-gradient(90deg,#cdb27a 0 8%,#f2ece0 8% 92%,#cdb27a 92%)"></div></div>
</section>

<section>
  <div class="abs contact-bg"></div>
  <h2 class="abs section-title" style="top:1950px;color:#fff">CONTACT</h2>
  <div class="abs sub" style="left:110px">CONTACT FORM</div>
  <div class="abs sub" style="left:744px">LOCATION</div>
  <div class="abs field" style="left:112px;top:2111px;width:286px;height:48px">First Name*</div>
  <div class="abs field" style="left:408px;top:2111px;width:288px;height:48px">Last Name*</div>
  <div class="abs field" style="left:112px;top:2170px;width:286px;height:48px">Email*</div>
  <div class="abs field" style="left:408px;top:2170px;width:288px;height:48px">Phone*</div>
  <div class="abs field" style="left:112px;top:2231px;width:586px;height:108px">Message</div>
  <div class="abs btn send">SEND</div>
  <div class="abs map" role="img" aria-label="Street map showing the company location"></div>

  <svg class="abs" style="left:0;top:2433px" width="1200" height="389"><path d="M0 135 L600 0 L1200 135 V389 H0Z" fill="#fff"/></svg>
  <div class="abs footer-logo"><div class="brand"><span>ORV</span><span class="dot"></span></div></div>

  <div class="abs info" style="left:158px">
    <div class="ring"><svg width="16" height="22" viewBox="0 0 16 22"><path d="M8 1a7 7 0 00-7 7c0 5 7 13 7 13s7-8 7-13a7 7 0 00-7-7z" fill="#3cc186"/><circle cx="8" cy="8" r="2.5" fill="#fff"/></svg></div>
    <div>14 Rue des Tilleuls<br>38100 VAL-DES-PINS</div>
  </div>
  <div class="abs info" style="left:475px;top:2643px">
    <div class="ring"><svg width="20" height="20" viewBox="0 0 24 24"><path fill="#3cc186" d="M6.6 10.8a15 15 0 006.6 6.6l2.2-2.2c.3-.3.7-.4 1-.2 1.1.4 2.3.6 3.6.6.6 0 1 .4 1 1V20c0 .6-.4 1-1 1A17 17 0 013 4c0-.6.4-1 1-1h3.5c.6 0 1 .4 1 1 0 1.3.2 2.5.6 3.6.1.3 0 .7-.2 1z"/></svg></div>
    <div>04 71 23 45 60</div>
  </div>
  <div class="abs info" style="left:672px">
    <div class="ring"><svg width="20" height="20" viewBox="0 0 20 20"><rect x="2" y="6" width="16" height="12" fill="#3cc186"/><rect x="5" y="2" width="8" height="5" fill="none" stroke="#3cc186" stroke-width="2"/><rect x="5" y="9" width="3" height="2" fill="#fff"/><rect x="10" y="9" width="3" height="2" fill="#fff"/><rect x="5" y="13" width="3" height="2" fill="#fff"/><rect x="10" y="13" width="3" height="2" fill="#fff"/></svg></div>
    <div>04 71 23 45 61</div>
  </div>
  <div class="abs info" style="left:869px">
    <div class="ring"><svg width="20" height="15" viewBox="0 0 16 12"><rect width="16" height="12" fill="#3cc186"/><path d="M0 0l8 6 8-6" stroke="#fff" stroke-width="1.5" fill="none"/></svg></div>
    <div>04 71 23 45 60</div>
  </div>

  <div class="abs links">Home<span>|</span>About us<span>|</span>Services<span>|</span>Achievements<span>|</span>Contact</div>
  <div class="abs copy">Copyright © 2020 ORV.</div>
  <div class="abs social"><span></span><span></span><span></span></div>
</section>

</body>
</html>
```